Web design for Crowdfunding site HaloFundry.com

We need a web design for christian crowdfunding website. Here is the challenge: We need responsive layout that is targeted first in iPad size of screen. It should also scale somehow down to iPhone size of screens. Web layout can be about the same size as iPad screen.

Screens should work so that main page scrolls not but only certain part of the screen scrolls and always one "page" at time. We can implement these "scrolls" then later with javascript but now we need only design. The challenge is to create this kind of hybrid website / app look.

Target is at first to raise funds to orphan people needing about $40 per month for their living and education. There is always some organization which takes care of these kids. Later there will be other christian missions included. At first we are looking to find monthly supporters.

You can be as creative as you want :) As you see from the look and feel sector, I am not looking any same traditional look which many "help kids" sites have. I am looking to reach now younger generation and therefore iPad and mobile are the main screen sizes.

Inspirational designs:
- https://brightpixelhub.example/profiles/studiokelvira/designs/418263?from=%2Fbrowse%2Fxhr%2Fdesigns%3Fcategory%3Dmobile-app-design
- http://www.artmarketloop.example/design/7261540 Clear, simple visuals
- http://www.artmarketloop.example/design/8420917 Header
- http://www.artmarketloop.example/design/6394275 Contrast in the colors, i think is powerfull

Some terms could be: Kids play, kids are learning (in the school). No static posture but living like kids are. I wonder also how we could also add little bit gaming style even though the question is of reali life of real people. Giving should be rewarding.

Target Market(s)

People who want help other people.

Industry/Entity Type

Christian

Number of Pages Required

4 page

Requirements
Must have
• Homepage. Mission page (In my wireframes it was one kid).
Nice to have
• Other pages and some idea how to scroll. 4 pages is no must. If you feel easy, please give first some draft and I give comments on that.

```html
<!DOCTYPE html>
<html lang="en">
<head>
<meta charset="utf-8">
<title>HaloFundry – Home</title>
<link href="https://fonts.googleapis.com/css2?family=Michroma&family=Lato:wght@400;700&display=swap" rel="stylesheet">
<style>
:root{
  --ink:#3a3a3a;
  --muted:#777;
  --white:#ffffff;
  --blue:#2f8fd8;
  --line:#4a4a4a;
  --green:#2fc48d;
  --ring:#e2592d;
  --disc:#6b3a22;
  --icon:#8fc7e8;
  --panel:#f4f4f4;
  --display:'Michroma',sans-serif;
  --body:'Lato',sans-serif;
}
*{box-sizing:border-box;margin:0;padding:0}
html,body{width:1200px;height:737px;overflow:hidden;background:var(--white)}
body{font-family:var(--body);color:var(--ink)}
.page{width:1200px;height:737px;display:flex;flex-direction:column}

/* header */
.site-header{height:66px;display:flex;align-items:center;padding:0 34px;border-bottom:1px solid #e6e6e6}
.brand{display:flex;align-items:center;gap:10px;margin-right:36px}
.brand-mark{width:14px;height:14px;border-radius:50%;background:var(--blue)}
.brand-name{font-family:var(--display);font-size:15px;line-height:1.15;color:#555;letter-spacing:.5px}
.main-nav{display:flex}
.main-nav a{display:block;text-decoration:none;text-align:center;padding:0 16px;border-left:2px solid var(--line)}
.main-nav a:first-child{border-left:none}
.nav-title{display:block;font-family:var(--display);font-size:11px;color:var(--ink);letter-spacing:1px}
.nav-sub{display:block;font-size:11px;color:var(--muted);margin-top:3px}
.account{margin-left:auto;display:flex;align-items:center;gap:12px}
.account .divider{width:2px;height:34px;background:var(--line)}
.login{font-family:var(--display);font-size:11px;color:var(--ink);letter-spacing:1px}
.login span{font-family:var(--body);font-size:11px;color:var(--muted);margin-left:6px}
.join{background:var(--blue);color:var(--white);font-family:var(--display);font-size:11px;padding:6px 20px;border-radius:3px}

/* hero */
.hero{position:relative;height:336px;overflow:hidden}
.hero-photo{position:absolute;inset:0;background:linear-gradient(120deg,#3f5a36 0%,#8a6a5a 30%,#c4566e 55%,#3d4a86 80%,#4a5a3e 100%)}
.hero-shade{position:absolute;inset:0;background:rgba(0,0,0,.25)}
.hero-copy{position:absolute;top:62px;left:0;right:0;text-align:center;color:var(--white)}
.hero-kicker{font-family:var(--display);font-size:15px;letter-spacing:1px}
.hero-title{font-family:var(--display);font-size:24px;letter-spacing:1px;margin-top:6px}
.hero-text{width:760px;margin:12px auto 0;font-size:12.5px;line-height:1.45}
.arrow{position:absolute;top:140px;width:22px;height:30px}
.arrow.prev{left:18px}.arrow.next{right:18px}
.stats{position:absolute;left:110px;right:90px;bottom:62px;height:58px;background:var(--white);display:flex;align-items:center;padding-left:240px}
.stat{flex:0 0 auto;text-align:center;padding:0 34px;border-left:2px solid var(--line)}
.stat:first-child{border-left:none}
.stat b{display:block;font-family:var(--display);font-size:17px;color:var(--ink);font-weight:400}
.stat small{display:block;font-size:11px;letter-spacing:1px;margin-top:2px}
.progress{position:absolute;left:170px;bottom:28px;width:120px;height:120px}
.progress-label{position:absolute;inset:0;display:flex;flex-direction:column;align-items:center;justify-content:center;color:var(--white)}
.progress-label b{font-family:var(--display);font-size:18px;font-weight:400}
.progress-label small{font-size:10px;letter-spacing:.5px}
.thumb{position:absolute;left:156px;bottom:22px;width:46px;height:46px;border-radius:50%;border:2px solid var(--white);background:linear-gradient(135deg,#c9a07a,#5a7a9a)}
.dots{position:absolute;bottom:14px;left:0;right:0;display:flex;justify-content:center;gap:6px}
.dots i{width:8px;height:8px;border-radius:50%;background:var(--white)}
.dots i:first-child{background:var(--green)}

/* welcome */
.welcome{height:190px;text-align:center;padding-top:18px}
.welcome h2{font-family:var(--display);font-size:13px;font-weight:400;line-height:1.45;letter-spacing:.5px}
.features{display:flex;justify-content:center;align-items:flex-start;gap:20px;margin-top:14px}
.feature{width:170px}
.feature-icon{width:52px;height:52px;margin:0 auto;border:2px solid var(--icon);border-radius:50%;display:flex;align-items:center;justify-content:center}
.plus{color:var(--green);font-size:30px;line-height:52px;font-weight:700}
.feature h3{font-family:var(--display);font-size:8px;font-weight:400;margin-top:10px;letter-spacing:.5px}
.feature hr{width:34px;border:none;height:2px;margin:4px auto}
.feature p{font-size:9px;color:var(--muted);line-height:1.35}

/* popular */
.popular{flex:1;background:var(--panel);text-align:center;padding-top:12px}
.popular h2{font-family:var(--display);font-size:12px;font-weight:400}
.cards{display:flex;justify-content:center;gap:14px;margin-top:10px}
.card{width:200px;background:var(--white)}
.card-photo{height:66px}
.card h4{font-family:var(--display);font-size:7px;font-weight:400;padding-top:6px}
.card hr{width:30px;border:none;height:2px;margin:4px auto}
.card p{font-size:8.5px;color:var(--muted);padding-bottom:4px}
</style>
</head>
<body>
<div class="page">
  <header class="site-header">
    <div class="brand"><span class="brand-mark"></span><span class="brand-name">HALO<br>FUNDRY</span></div>
    <nav class="main-nav">
      <a href="#"><span class="nav-title">ABOUT</span><span class="nav-sub">what is funds</span></a>
      <a href="#"><span class="nav-title">EXPLORE</span><span class="nav-sub">amazing ideas</span></a>
      <a href="#"><span class="nav-title">START</span><span class="nav-sub">send your idea</span></a>
    </nav>
    <div class="account">
      <svg width="22" height="22" viewBox="0 0 22 22" fill="none" stroke="#555" stroke-width="2"><circle cx="9" cy="9" r="6.5"/><line x1="14" y1="14" x2="20" y2="20"/></svg>
      <span class="divider"></span>
      <span class="login">LOGIN<span>OR</span></span>
      <span class="join">JOIN</span>
    </div>
  </header>

  <section class="hero">
    <div class="hero-photo" role="img" aria-label="Photo of three young sisters smiling together on a porch"></div>
    <div class="hero-shade"></div>
    <div class="hero-copy">
      <p class="hero-kicker">OUR MISSION</p>
      <h1 class="hero-title">FOR LITTLE ANGELS</h1>
      <p class="hero-text">Pellentesque pharetra sapien non quam placerat vestibulum. Aliquam dignissim ex nec feugiat condimentum. Sed iaculis magna mi, ex semper eu. Etiam sagittis ante eget nisi tempus, elementum sollicitudin nulla lacinia. Aenean sed odio ipsum. Nam tincidunt, sed ultricies nisl tristique eget. Vestibulum auctor mi sed sapien hendrerit, et auctor nulla egestas. Maecenas facilisis.</p>
    </div>
    <svg class="arrow prev" viewBox="0 0 22 30" fill="none" stroke="#fff" stroke-width="3"><polyline points="15,5 6,15 15,25"/></svg>
    <svg class="arrow next" viewBox="0 0 22 30" fill="none" stroke="#fff" stroke-width="3"><polyline points="7,5 16,15 7,25"/></svg>
    <div class="stats">
      <div class="stat"><b>12</b><small>DAYS LEFT</small></div>
      <div class="stat"><b>175</b><small>BACKERS</small></div>
      <div class="stat"><b>R$7000,00</b><small>FUNDED</small></div>
    </div>
    <div class="progress">
      <svg width="120" height="120" viewBox="0 0 120 120">
        <circle cx="60" cy="60" r="54" fill="none" stroke="#f1e3da" stroke-width="8"/>
        <circle cx="60" cy="60" r="54" fill="none" stroke="var(--ring)" stroke-width="8" stroke-dasharray="254.5 339.3" transform="rotate(-90 60 60)"/>
        <circle cx="60" cy="60" r="48" fill="var(--disc)"/>
      </svg>
      <div class="progress-label"><b>75%</b><small>COMPLETED</small></div>
    </div>
    <div class="thumb" role="img" aria-label="Small portrait photo of a child"></div>
    <div class="dots"><i></i><i></i><i></i></div>
  </section>

  <section class="welcome">
    <h2>Welcome to Halo Fundry<br>Its a crowdfunding</h2>
    <div class="features">
      <div class="feature">
        <div class="feature-icon"><svg width="24" height="24" viewBox="0 0 24 24" fill="none" stroke="var(--icon)" stroke-width="1.6"><path d="M8 14a6 6 0 1 1 8 0v3H8z"/><line x1="9" y1="20" x2="15" y2="20"/><line x1="12" y1="1" x2="12" y2="3"/><line x1="3" y1="9" x2="5" y2="9"/><line x1="19" y1="9" x2="21" y2="9"/></svg></div>
        <h3>AMAZING IDEAS</h3><hr style="background:var(--green)">
        <p>Pellentesque pharetra sapien non quam placerat vestibulum.</p>
      </div>
      <span class="plus">+</span>
      <div class="feature">
        <div class="feature-icon"><svg width="24" height="24" viewBox="0 0 24 24" fill="none" stroke="var(--icon)" stroke-width="1.6"><circle cx="12" cy="8" r="4"/><path d="M4 21c0-4.5 3.6-7 8-7s8 2.5 8 7"/></svg></div>
        <h3>COMMUNITY</h3><hr style="background:#f2b233">
        <p>Pellentesque pharetra sapien non quam placerat vestibulum.</p>
      </div>
      <span class="plus">+</span>
      <div class="feature">
        <div class="feature-icon"><svg width="24" height="24" viewBox="0 0 24 24" fill="none" stroke="var(--icon)" stroke-width="1.6"><rect x="5" y="3" width="14" height="18" rx="1"/><line x1="8" y1="8" x2="16" y2="8"/><line x1="8" y1="12" x2="16" y2="12"/><line x1="8" y1="16" x2="13" y2="16"/></svg></div>
        <h3>PUBLIC POWER</h3><hr style="background:var(--ring)">
        <p>Pellentesque pharetra sapien non quam placerat vestibulum.</p>
      </div>
    </div>
  </section>

  <section class="popular">
    <h2>Popular at HaloFundry</h2>
    <div class="cards">
      <article class="card"><div class="card-photo" role="img" aria-label="Photo of a smiling little girl outdoors" style="background:linear-gradient(135deg,#6f9a4a,#d8c0a8)"></div><h4>MARIA (Ophan, Jacob)</h4><hr style="background:var(--green)"><p>Pellentesque pharetra sapien</p></article>
      <article class="card"><div class="card-photo" role="img" aria-label="Photo of a smiling child in a garden" style="background:linear-gradient(135deg,#7aa040,#c89a70)"></div><h4>MATHEW (Ophan, Jacob)</h4><hr style="background:#f2b233"><p>Pellentesque pharetra sapien</p></article>
      <article class="card"><div class="card-photo" role="img" aria-label="Photo of a fair-haired girl portrait" style="background:linear-gradient(135deg,#8a8a5a,#d8b890)"></div><h4>MARIA (Ophan, Jacob)</h4><hr style="background:var(--ring)"><p>Pellentesque pharetra sapien</p></article>
      <article class="card"><div class="card-photo" role="img" aria-label="Photo of a dark-haired girl smiling outdoors" style="background:linear-gradient(135deg,#5a8a3a,#b07a5a)"></div><h4>MATHEW (Ophan, Jacob)</h4><hr style="background:#e04a6a"><p>Pellentesque pharetra sapien</p></article>
    </div>
  </section>
</div>
</body>
</html>
```